Design of Labels for Harbour Mast Spirit bottle

Design bottle labels for Harbour Mast Spirit. There are three labels to design; a front, a back and a tamper band to be placed over the cork. The labels should be deigned to fit the bottle specified in the link below.
The Gin is an excellent high end premium brand Navy strength Gin 57% Vol. The bottle should evoke excellence and a romance of period of pride in the British Navy. Gin was drunk by officers in the Navy so a representation of the Officer Class should be made possibly through gold braid of a senior officer's sleeve, cap or lapel. The white ensign should also be prominent. Suggested colour themes are navy blues, grey, and white....although others schemes may be suitable. Crowfield Deck Cordial is a good example of the sort of thing we are looking for, although the design must not be so similar that it encroaches on Crowfield's trade mark or copyrights. The period theme is 1900 to 1940
Bottle link: https://www.vessel-ware-depot.co.uk/Glass-bottles/350ml-flint-glass-bottle-Mirren.html
Target Market(s)
Gin Drinkers
Look and feel
Each slider illustrates characteristics of the customer's brand and the style your logo design should communicate.

```html
<!DOCTYPE html>
<html lang="en">
<head>
<meta charset="utf-8">
<title>Harbour Mast Spirit – Front Label</title>
<link rel="stylesheet" href="https://fonts.googleapis.com/css2?family=Montserrat:wght@300;400;800&family=Great+Vibes&display=swap">
<style>
  :root {
    --backdrop: #1c1c1e;
    --label-blue-light: #2f6fd6;
    --label-blue: #1f56b8;
    --label-blue-deep: #133a86;
    --braid-gold: #e8c23a;
    --ink-white: #f4f6fb;
    --ink-navy: #0f2f78;
    --flag-white: #e9ecf4;
    --ship-navy: #13306e;
  }
  * { margin: 0; padding: 0; box-sizing: border-box; }
  html, body { width: 1200px; height: 1000px; overflow: hidden; }
  body {
    background: var(--backdrop);
    font-family: "Montserrat", sans-serif;
    position: relative;
  }
  .front-label {
    position: absolute;
    left: 350px;
    top: 150px;
    width: 500px;
    height: 700px;
    color: var(--ink-white);
    text-align: center;
  }
  .label-shape { position: absolute; inset: 0; width: 500px; height: 700px; }
  .crown-icon {
    position: absolute; left: 225px; top: 28px; width: 50px; height: 36px;
  }
  .ensign-flag {
    position: absolute; left: 150px; top: 95px; width: 200px; height: 70px;
    background: linear-gradient(100deg, var(--flag-white), #d3d8e6);
    border-radius: 3px;
  }
  .brand-name {
    position: absolute; left: 40px; right: 40px; top: 185px;
    font-weight: 800; font-size: 54px; line-height: 56px;
    letter-spacing: 1px; color: var(--ink-white);
  }
  .ship-illustration {
    position: absolute; left: 130px; top: 370px; width: 240px; height: 80px;
    background: linear-gradient(180deg, rgba(19,48,110,0.35), var(--ship-navy));
    border-radius: 4px 4px 30px 30px;
  }
  .script-line {
    position: absolute; left: 0; right: 0;
    font-family: "Great Vibes", cursive; font-size: 36px; line-height: 40px;
  }
  .script-line.quality { top: 462px; color: var(--ink-white); }
  .script-line.strength { top: 500px; color: var(--ink-navy); font-size: 30px; }
  .product-type {
    position: absolute; left: 0; right: 0; top: 540px;
    font-weight: 400; font-size: 54px; letter-spacing: 2px;
  }
  .strength-abv {
    position: absolute; left: 0; right: 0; top: 610px;
    font-weight: 300; font-size: 20px;
  }
  .volume {
    position: absolute; left: 34px; top: 620px;
    font-weight: 300; font-size: 14px;
  }
  .anchor-icon {
    position: absolute; left: 232px; top: 650px; width: 36px; height: 36px;
  }
</style>
</head>
<body>
  <section class="front-label">
    <svg class="label-shape" viewBox="0 0 500 700" aria-hidden="true">
      <defs>
        <linearGradient id="labelFill" x1="0" y1="0" x2="0" y2="1">
          <stop offset="0" stop-color="var(--label-blue-light)"/>
          <stop offset="0.55" stop-color="var(--label-blue)"/>
          <stop offset="1" stop-color="var(--label-blue-deep)"/>
        </linearGradient>
      </defs>
      <path d="M10,110 Q55,104 70,55 Q250,0 430,55 Q445,104 490,110 L490,630 L250,695 L10,630 Z"
            fill="url(#labelFill)" stroke="var(--ink-navy)" stroke-width="4"/>
      <path d="M24,120 Q65,114 80,68 Q250,16 420,68 Q435,114 476,120 L476,620 L250,680 L24,620 Z"
            fill="none" stroke="var(--braid-gold)" stroke-width="4"/>
    </svg>

    <svg class="crown-icon" viewBox="0 0 50 36" aria-hidden="true">
      <path d="M4,28 L2,8 L14,18 L25,2 L36,18 L48,8 L46,28 Z" fill="var(--ink-white)"/>
      <rect x="4" y="30" width="42" height="5" fill="var(--ink-white)"/>
    </svg>

    <div class="ensign-flag" role="img" aria-label="White ensign flag illustration"></div>

    <h1 class="brand-name">HARBOUR MAST SPIRIT</h1>

    <div class="ship-illustration" role="img" aria-label="Illustration of a period naval sailing warship"></div>

    <p class="script-line quality">Premium Quality</p>
    <p class="script-line strength">Navy Strength</p>

    <p class="product-type">GIN</p>
    <p class="strength-abv">57%vol</p>
    <p class="volume">e35ml</p>

    <svg class="anchor-icon" viewBox="0 0 36 36" aria-hidden="true">
      <g fill="none" stroke="var(--ink-white)" stroke-width="3" stroke-linecap="round">
        <circle cx="18" cy="5" r="3"/>
        <line x1="18" y1="8" x2="18" y2="33"/>
        <line x1="11" y1="13" x2="25" y2="13"/>
        <path d="M4,20 Q6,32 18,33 Q30,32 32,20"/>
      </g>
    </svg>
  </section>
</body>
</html>
```